CLU大学院「スキル羅針盤」のバナー作成 を作成していただける方を募集しております。 ■目的・概要 MBA取得検討者向け、ターゲティング広告用に、 コスモリンク大学大学院がプロデュースした「スキル羅針盤」の 新しいバナーの作成依頼です。 ■デザインイメージ 既存のバナーをご参考までに貼付いたします。 このバナーと同等かもしくはそれを上回るクオリティでの作成ができればと思います。 ランディング先のページは下記です。 サイト名:スキル羅針盤 URL: http://www.cosmolink-u.example/sk_lp/ スキル羅針盤は2万人を超える方々が実施しているコンテンツですので、 「診断者数2万人」などの要素をバナー内に入れていただいても結構です。 基本的には製作者様のセンスにお任せしたいと思います。 ■サイズ: 300×250 1枚 ■値段: 5000円 ■納品形式: PSDデータとJPGデータ ■継続について 今回コンペで採用された方には、引き続き他の10個以上のバナーの作成をお願いすることになるので、 ぜひふるってご応募くださいませ! 素敵なバナーになるよう、ぜひお力を貸してください。 たくさんのご応募お待ち致しております! |

```html
<!DOCTYPE html>
<html lang="ja">
<head>
<meta charset="utf-8">
<title>スキル羅針盤 バナー</title>
<link href="https://fonts.googleapis.com/css2?family=Noto+Sans+JP:wght@500;700;900&family=Roboto:wght@500;700&display=swap" rel="stylesheet">
<style>
  :root {
    --page: #ffffff;
    --frame: #b9b9b9;
    --maroon-dark: #3d0606;
    --maroon: #7a1313;
    --maroon-light: #a8322a;
    --red: #d8141b;
    --gold-light: #fff3c4;
    --gold: #e2bb5c;
    --gold-dark: #8a5a12;
    --white: #ffffff;
    --ink: #1a1a1a;
    --logo-blue: #1c7fc4;
  }
  * { box-sizing: border-box; margin: 0; padding: 0; }
  html, body {
    width: 1200px; height: 1007px; overflow: hidden;
    background: var(--page);
    font-family: "Noto Sans JP", sans-serif;
    font-feature-settings: "palt";
  }
  .banner {
    position: absolute; left: 91px; top: 92px;
    width: 1018px; height: 822px;
    border: 2px solid var(--frame);
    background: var(--white);
    overflow: hidden;
  }
  .hero {
    position: absolute; left: 8px; top: 8px; right: 8px; height: 670px;
    background:
      radial-gradient(ellipse at 30% 35%, rgba(168,50,42,.55), transparent 60%),
      linear-gradient(160deg, var(--maroon-light) 0%, var(--maroon) 40%, var(--maroon-dark) 100%);
  }
  .ribbon {
    position: absolute; left: 508px; top: 22px; width: 440px; height: 80px;
    background: linear-gradient(180deg, var(--gold-light), var(--gold) 55%, #b98a2c);
    transform: rotate(-4deg);
    box-shadow: 0 4px 8px rgba(0,0,0,.45);
    display: flex; align-items: center; justify-content: center;
    color: var(--red); font-weight: 900; font-size: 46px; white-space: nowrap;
  }
  .question {
    position: absolute; left: 420px; top: 120px; right: 0; height: 58px;
    background: var(--red);
    color: var(--white); font-weight: 900; font-size: 33px; white-space: nowrap;
    display: flex; align-items: center; padding-left: 22px;
  }
  .lead {
    position: absolute; left: 40px; top: 210px; width: 940px;
    color: var(--white); font-weight: 900; font-size: 43px; white-space: nowrap;
    text-shadow: 0 3px 6px rgba(0,0,0,.6);
  }
  .title {
    position: absolute; left: 0; top: 282px; width: 100%; text-align: center;
    font-weight: 900; font-size: 150px; line-height: 1.1; letter-spacing: -2px; white-space: nowrap;
    background: linear-gradient(180deg, var(--gold-light) 10%, var(--gold) 50%, var(--gold-dark) 100%);
    -webkit-background-clip: text; background-clip: text; color: transparent;
    filter: drop-shadow(0 5px 4px rgba(0,0,0,.7));
  }
  .tagline {
    position: absolute; left: 0; top: 480px; width: 100%; text-align: center;
    color: var(--white); font-family: "Roboto", sans-serif; font-weight: 500; font-size: 36px;
  }
  .cta {
    position: absolute; left: 33px; top: 563px; width: 355px; height: 72px;
    border-radius: 8px;
    background: linear-gradient(180deg, var(--gold-light), var(--gold) 55%, #a87822);
    color: var(--ink); font-weight: 900; font-size: 38px; white-space: nowrap;
    display: flex; align-items: center; justify-content: center; gap: 14px;
    box-shadow: 0 3px 6px rgba(0,0,0,.5);
  }
  .cta svg { width: 26px; height: 30px; }
  .accuracy {
    position: absolute; left: 425px; top: 548px;
    font-weight: 900; font-size: 46px; white-space: nowrap;
    background: linear-gradient(180deg, var(--gold-light) 15%, var(--gold) 60%, #b4832a);
    -webkit-background-clip: text; background-clip: text; color: transparent;
  }
  .accuracy .num { font-family: "Roboto", sans-serif; font-weight: 700; font-size: 84px; }
  .school {
    position: absolute; left: 8px; right: 8px; top: 686px; bottom: 8px;
    display: flex; align-items: center; gap: 30px; padding-left: 40px;
  }
  .school-mark { width: 90px; height: 90px; border-radius: 50%; background: var(--logo-blue); flex: none; }
  .school-name { color: var(--ink); font-weight: 700; font-size: 52px; line-height: 1.15; white-space: nowrap; }
  .school-name-en { display: block; font-family: "Roboto", sans-serif; font-weight: 500; font-size: 32px; letter-spacing: .5px; }
</style>
</head>
<body>
  <div class="banner">
    <div class="hero" role="img" aria-label="赤みがかった背景に、ビジネスパーソンのシルエット写真"></div>
    <div class="ribbon">診断者数2万人!</div>
    <div class="question">キャリアアップのために何が必要か!</div>
    <p class="lead">「ビジネス能力」と「志向特性」をあぶりだす!?</p>
    <h1 class="title">スキル羅針盤</h1>
    <p class="tagline">~Find Your Direction~</p>
    <div class="cta">詳しくはこちら
      <svg viewBox="0 0 26 30"><polygon points="0,0 26,15 0,30" fill="#1a1a1a"/></svg>
    </div>
    <p class="accuracy">診断結果整合率<span class="num">84</span>%</p>
    <div class="school">
      <span class="school-mark"></span>
      <p class="school-name">コスモリンク大学大学院
        <span class="school-name-en">Cosmolink Graduate School of Business</span>
      </p>
    </div>
  </div>
</body>
</html>
```